Consulting company needs website design

We need a simple, static website design for our consulting company. We are looking for a general design of the look and feel of the website. Initially, it will have these pages:
- Home
- About us
- Services
- Contact us
We have our own logo which I have attached to the brief.

We are looking for a simple website, with white background and the use of gray (darker) as the main theme. Simple fonts. The website should be responsive so it an be easily red in mobile devices.

As part of the project, we will need to receive at least the following items:
- Individual files with sample text to support the pages outlined above
- Necessary CSS files

Our current website is here: http://www.marlowvane.co/

Here are some examples of other website we like to be used as guideline:
- http://www.tornaviamundo.com/
-

Target Market(s)

Individuals and companies looking to hire our company to provide consulting services.

Industry/Entity Type

It Company

Coding

Coded - Design and coding required

Number of Pages Required

4 page

Font styles to use
Sans Serif

Requirements
Must have
• Main page should have the ability to embed Chirply feed into it.
• We prefer the design to use gray tones.

```html
<!DOCTYPE html>
<html lang="en">
<head>
<meta charset="utf-8">
<title>Marlowvane Group SAS</title>
<link rel="stylesheet" href="https://fonts.googleapis.com/css2?family=Open+Sans:ital,wght@0,400;0,600;0,700;1,400&display=swap">
<style>
:root{
  --ink:#2b2b2b;
  --text:#444;
  --muted:#777;
  --line:#cfcfcf;
  --panel:#e8e8e8;
  --card:#e2e2e2;
  --dark:#222;
  --black:#0d0d0d;
  --white:#fff;
  --btn-top:#5a5a5a;
  --btn-bottom:#2e2e2e;
}
*{margin:0;padding:0;box-sizing:border-box}
html,body{width:1200px;height:2356px;overflow:hidden}
body{font-family:"Open Sans",Arial,sans-serif;color:var(--text);background:var(--white);position:relative}
.abs{position:absolute}

/* hero */
.hero{position:absolute;left:0;top:0;width:1200px;height:652px;
  background:linear-gradient(180deg,#6f7a86 0%,#8b96a0 30%,#3c4046 60%,#1c1d20 100%)}
.hero-glow{position:absolute;left:0;top:0;width:1200px;height:652px;
  background:radial-gradient(circle at 560px 380px,rgba(255,230,170,.55) 0,rgba(255,230,170,0) 200px)}
.caption-band{position:absolute;left:0;top:0}
.hero-title{left:100px;top:550px;font-size:31px;font-weight:700;color:var(--white);letter-spacing:.5px}
.hero-text{left:100px;top:592px;width:560px;font-size:13.5px;line-height:19px;color:#ddd}
.hero-arrows{left:1058px;top:618px;color:var(--white);font-size:26px;letter-spacing:10px}
.hero-arrows span:first-child{color:#888}

/* header */
.brand{left:94px;top:8px;width:160px;height:152px;border-radius:50%;background:var(--white);
  display:flex;align-items:center;justify-content:center;font-size:20px;font-weight:600;color:var(--ink)}
.topbar{left:157px;top:44px;width:944px;height:79px;background:var(--white);border-radius:5px;
  box-shadow:0 2px 6px rgba(0,0,0,.25)}
.nav{position:absolute;left:130px;top:0;height:79px;display:flex;align-items:center;font-size:14px;color:var(--ink)}
.nav a{color:inherit;text-decoration:none;padding:0 20px;height:79px;display:flex;align-items:center;border-right:1px solid #ddd}
.nav a:last-child{border-right:0}
.nav .is-home{font-weight:700;padding-left:0}
.nav .is-active{background:#2f2f2f;color:var(--white)}
.contact-bit{position:absolute;top:22px;display:flex;align-items:center;gap:10px}
.contact-bit small{display:block;font-size:8.5px;font-weight:700;color:var(--ink);letter-spacing:.2px}
.contact-bit strong{display:block;font-size:16px;font-weight:400;color:var(--ink);line-height:18px}
.bar-divider{position:absolute;left:560px;top:18px;width:1px;height:44px;background:#ccc}

/* headings */
.section-title{position:absolute;left:0;width:1200px;text-align:center;font-size:31px;font-weight:700;color:var(--ink);letter-spacing:.5px}
.title-rule{position:absolute;left:523px;width:156px;height:1px;background:var(--line)}
.title-rule::after{content:"";position:absolute;left:52px;top:-1px;width:52px;height:3px;background:var(--ink)}

/* about */
.about-text{left:107px;top:766px;width:988px;text-align:center;font-size:13.4px;line-height:24.5px;color:var(--text)}
.read-more{left:540px;top:911px;width:120px;height:38px;background:linear-gradient(var(--btn-top),var(--btn-bottom));
  color:var(--white);font-size:13px;font-weight:700;display:flex;align-items:center;justify-content:center;border-radius:2px}

/* services */
.services{position:absolute;left:0;top:993px;width:1200px;height:750px;background:var(--panel)}
.services svg text{font-family:"Open Sans",Arial,sans-serif;font-size:17px;font-weight:600;fill:#333}

/* testimonials */
.quote-card{left:0;top:0}
.client-photo{left:102px;top:1908px;width:104px;height:104px;border-radius:50%;
  background:linear-gradient(160deg,#c9b8a6,#7e6d60);border:4px solid var(--white)}
.quote-badge{left:210px;top:1922px;width:76px;height:76px;border-radius:50%;background:#000;border:4px solid var(--white);
  color:var(--white);font-size:70px;font-weight:700;line-height:100px;text-align:center;font-family:Georgia,serif}
.quote-mark{left:312px;top:1892px;font-size:52px;color:#b5b5b5;font-family:Georgia,serif;font-weight:700}
.quote-text{left:355px;top:1904px;width:690px;font-size:14px;font-style:italic;line-height:24px;color:#555}
.quote-author{left:700px;top:1968px;width:288px;text-align:right;font-size:15px;color:#222}
.slide-btn{left:1061px;width:34px;height:34px;border-radius:50%;background:#8a8a8a;color:var(--white);
  font-size:13px;display:flex;align-items:center;justify-content:center}

/* footer */
.site-footer{left:0;top:2098px;width:1200px;height:214px;background:var(--dark)}
.footer-mark{left:123px;top:2157px;width:100px;height:100px;border-radius:50%;background:var(--white)}
.footer-name{left:236px;top:2168px;font-size:29px;line-height:41px;color:var(--muted)}
.footer-divider{top:2144px;width:1px;height:118px;background:#3a3a3a}
.footer-badge{top:2147px;width:88px;height:88px}
.footer-label{top:2247px;width:240px;text-align:center;font-size:14px;color:#ccc}
.copyright{left:0;top:2312px;width:1200px;height:44px;background:var(--black);color:var(--white);
  font-size:12px;font-weight:700;display:flex;align-items:center;justify-content:center}
</style>
</head>
<body>

<header>
  <div class="hero" role="img" aria-label="Photo of business people shaking hands in front of a bright office window with a city skyline"></div>
  <div class="hero-glow"></div>
  <svg class="caption-band" width="1200" height="652" aria-hidden="true">
    <polygon points="0,531 600,531 645,609 1200,609 1200,652 0,652" fill="rgba(0,0,0,.78)"/>
  </svg>
  <h1 class="abs hero-title">TALANTED CONSULTANTS</h1>
  <p class="abs hero-text">Lorem ipsum dolor sit amet, consectetur adipiscing elit. Nunc facilisis fringilla nisi euismod Morbi sed adipiscing eleifend, dolor risus congue mi alique.</p>
  <div class="abs hero-arrows"><span>&#8249;</span><span>&#8250;</span></div>

  <div class="abs topbar">
    <nav class="nav">
      <a class="is-home">HOME</a>
      <a>ABOUT US</a>
      <a class="is-active">SERVICES &#8964;</a>
      <a>CONTACT US</a>
    </nav>
    <div class="bar-divider"></div>
    <div class="contact-bit" style="left:590px">
      <svg width="24" height="24" viewBox="0 0 24 24" aria-hidden="true"><path d="M6 2l4 4-2.5 2.5a12 12 0 0 0 8 8L18 14l4 4-3 3C10 21 3 14 3 5z" fill="none" stroke="#222" stroke-width="1.8" stroke-linejoin="round"/></svg>
      <div><small>CALL US TODAY</small><strong>123.456.7890</strong></div>
    </div>
    <div class="contact-bit" style="left:738px">
      <svg width="26" height="20" viewBox="0 0 26 20" aria-hidden="true"><rect x="1" y="1" width="24" height="18" rx="2" fill="none" stroke="#222" stroke-width="1.8"/><path d="M2 3l11 9 11-9" fill="none" stroke="#222" stroke-width="1.8"/></svg>
      <div><small>EMAIL US NOW</small><strong>info@marlowvane.com</strong></div>
    </div>
  </div>
  <div class="abs brand">Marlowvane</div>
</header>

<main>
  <section class="about">
    <h2 class="section-title" style="top:682px">ABOUT US</h2>
    <div class="title-rule" style="top:743px"></div>
    <p class="abs about-text">Lorem ipsum dolor sit amet, consectetuer adipiscing elit, sed diam nonummy nibh euismod tincidunt ut laoreet dolore magna aliquam erat volutpat. Ut wisi enim ad minim veniam, quis nostrud exerci tation ullamcorper suscipit lobortis nisl ut aliquip ex ea commodo consequat. Duis autem vel eum iriure dolor in hendrerit in vulputate velit esse molestie consequat, vel illum dolore eu feugiat nulla facilisis at vero eros et accumsan et iusto odio dignissim qui blandit praesent luptatum zzril delenit augue duis dolore te feugait nulla facilisi.Lorem ipsum dolong elit, sed diam nonummy nibh euismod tinciduntisi.Lorem ipsum dolong elit, sed diam nonummy nibh euismod tincidunt ut ut laoreet dolore magna aliquam erat volutpat.</p>
    <div class="abs read-more">Read More</div>
  </section>

  <section class="services">
    <h2 class="section-title" style="top:33px">OUR SERVICES</h2>
    <div class="title-rule" style="top:94px"></div>
    <svg width="1200" height="750" style="position:absolute;left:0;top:0">
      <defs>
        <g id="badge">
          <polygon points="54,0 46.8,27 27,46.8 0,54 -27,46.8 -46.8,27 -54,0 -46.8,-27 -27,-46.8 0,-54 27,-46.8 46.8,-27" fill="#f6f6f6" stroke="#6e6e6e" stroke-width="2" transform="rotate(15)"/>
          <polygon points="54,0 46.8,27 27,46.8 0,54 -27,46.8 -46.8,27 -54,0 -46.8,-27 -27,-46.8 0,-54 27,-46.8 46.8,-27" fill="none" stroke="#c4c4c4" stroke-width="1.5" transform="rotate(15) scale(.84)"/>
          <circle r="13" fill="#2a2a2a"/>
        </g>
      </defs>
      <g stroke="#555" stroke-width="1.6" stroke-dasharray="2 4" fill="none">
        <line x1="509" y1="177" x2="589" y2="429"/><line x1="666" y1="177" x2="589" y2="429"/>
        <line x1="379" y1="271" x2="589" y2="429"/><line x1="796" y1="271" x2="589" y2="429"/>
        <line x1="328" y1="416" x2="589" y2="416"/><line x1="848" y1="416" x2="589" y2="416"/>
        <line x1="379" y1="554" x2="589" y2="429"/><line x1="796" y1="554" x2="589" y2="429"/>
        <line x1="509" y1="648" x2="589" y2="429"/><line x1="666" y1="648" x2="589" y2="429"/>
      </g>
      <g stroke="#666" stroke-width="1.2" fill="none">
        <polyline points="353,150 440,150 460,165"/><polyline points="821,150 735,150 715,165"/>
        <polyline points="259,273 326,273"/><polyline points="914,273 850,273"/>
        <polyline points="229,416 274,416"/><polyline points="939,416 902,416"/>
        <polyline points="250,554 326,554"/><polyline points="914,554 850,554"/>
        <polyline points="353,675 440,675 460,662"/><polyline points="821,675 735,675 715,662"/>
      </g>
      <g fill="#222">
        <circle cx="353" cy="150" r="3"/><circle cx="821" cy="150" r="3"/>
        <circle cx="259" cy="273" r="3"/><circle cx="914" cy="273" r="3"/>
        <circle cx="229" cy="416" r="3"/><circle cx="939" cy="416" r="3"/>
        <circle cx="250" cy="554" r="3"/><circle cx="914" cy="554" r="3"/>
        <circle cx="353" cy="675" r="3"/><circle cx="821" cy="675" r="3"/>
      </g>
      <use href="#badge" x="509" y="177"/><use href="#badge" x="666" y="177"/>
      <use href="#badge" x="379" y="271"/><use href="#badge" x="796" y="271"/>
      <use href="#badge" x="328" y="416"/><use href="#badge" x="848" y="416"/>
      <use href="#badge" x="379" y="554"/><use href="#badge" x="796" y="554"/>
      <use href="#badge" x="509" y="648"/><use href="#badge" x="666" y="648"/>
      <circle cx="589" cy="416" r="122" fill="#fbfbfb" stroke="#9a9a9a" stroke-width="2"/>
      <text x="589" y="423" text-anchor="middle" style="font-size:24px">Marlowvane</text>
      <text x="339" y="156" text-anchor="end">Business Strategy</text>
      <text x="834" y="156">Corporate Governance</text>
      <text x="247" y="271" text-anchor="end">Corporate Social</text>
      <text x="247" y="292" text-anchor="end">Responsibility</text>
      <text x="928" y="265">Performance</text>
      <text x="928" y="286">Management</text>
      <text x="220" y="412" text-anchor="end">Ethics and</text>
      <text x="220" y="433" text-anchor="end">Compliance</text>
      <text x="953" y="412">Interim</text>
      <text x="953" y="433">Management</text>
      <text x="237" y="554" text-anchor="end">Supply Chain</text>
      <text x="237" y="575" text-anchor="end">Management</text>
      <text x="928" y="554">New Business</text>
      <text x="928" y="575">Development</text>
      <text x="339" y="681" text-anchor="end">Financial Management</text>
      <text x="834" y="681">Risk Management</text>
    </svg>
  </section>

  <section class="testimonials">
    <h2 class="section-title" style="top:1779px">CLIENTS TESTIMONIALS</h2>
    <div class="title-rule" style="top:1839px"></div>
    <svg class="abs quote-card" width="1200" height="2356" aria-hidden="true">
      <polygon points="190,1866 1072,1866 1079,1873 1079,2011 181,2054 181,1876" fill="var(--card)"/>
    </svg>
    <div class="abs client-photo" role="img" aria-label="Portrait of the client giving the testimonial"></div>
    <div class="abs quote-badge">&#8220;</div>
    <div class="abs quote-mark">&#8220;</div>
    <p class="abs quote-text">Lorem ipsum dolor smit amet, consectetuer adipiscing elitmk, sed amet diam nonummy nibh euismod tincidun nt ut looreetml dolore magna aliquam erat volutpat. Ut wisi enim ad minim veniam, quis nostrud exer tationk ullamcori per suscipit lobortisk nisl utml aliqpi ex ea commodo consequat. Duis autem.</p>
    <p class="abs quote-author">- Mrs. Elda Morrin</p>
    <div class="abs slide-btn" style="top:1924px">&gt;</div>
    <div class="abs slide-btn" style="top:1965px">&lt;</div>
  </section>
</main>

<footer>
  <div class="abs site-footer"></div>
  <div class="abs footer-mark"></div>
  <div class="abs footer-name">Marlowvane<br>Group SAS</div>
  <div class="abs footer-divider" style="left:424px"></div>
  <div class="abs footer-divider" style="left:776px"></div>
  <svg class="abs footer-badge" style="left:558px" viewBox="-44 -44 88 88" aria-hidden="true">
    <polygon points="42,0 36.4,21 21,36.4 0,42 -21,36.4 -36.4,21 -42,0 -36.4,-21 -21,-36.4 0,-42 21,-36.4 36.4,-21" fill="#fff" transform="rotate(15)"/>
    <polygon points="42,0 36.4,21 21,36.4 0,42 -21,36.4 -36.4,21 -42,0 -36.4,-21 -21,-36.4 0,-42 21,-36.4 36.4,-21" fill="none" stroke="#222" stroke-width="1.5" transform="rotate(15) scale(.86)"/>
    <path d="M-7,-10 l4,4 -2,2 a9 9 0 0 0 6,6 l2,-2 4,4 -2.5,2.5 C-4,6 -10,0 -10,-7z" fill="none" stroke="#222" stroke-width="1.6" stroke-linejoin="round"/>
  </svg>
  <svg class="abs footer-badge" style="left:900px" viewBox="-44 -44 88 88" aria-hidden="true">
    <polygon points="42,0 36.4,21 21,36.4 0,42 -21,36.4 -36.4,21 -42,0 -36.4,-21 -21,-36.4 0,-42 21,-36.4 36.4,-21" fill="#fff" transform="rotate(15)"/>
    <polygon points="42,0 36.4,21 21,36.4 0,42 -21,36.4 -36.4,21 -42,0 -36.4,-21 -21,-36.4 0,-42 21,-36.4 36.4,-21" fill="none" stroke="#222" stroke-width="1.5" transform="rotate(15) scale(.86)"/>
    <rect x="-11" y="-8" width="22" height="16" rx="1.5" fill="none" stroke="#222" stroke-width="1.6"/>
    <path d="M-10,-6 l10,8 10,-8" fill="none" stroke="#222" stroke-width="1.6"/>
  </svg>
  <div class="abs footer-label" style="left:482px">123.456.7890</div>
  <div class="abs footer-label" style="left:824px">info@marlowvane.com</div>
  <div class="abs copyright">Copyright © 2016 Marlowvane Group. All Right Reserved.</div>
</footer>

</body>
</html>
```